Professional, Attractive, Simple Website Needed!!

We completed the design for our logo.

We need a website built out around this.

Here are a couple samples of how we want ours formatted.

http://brvtawatt.com

http://www.brightmerlo.com/lp/free-quote?LeadSource=Search%20Engine&ProgramName=webfind&experience=qual&language=en&type=brd&gclid=Xq7LMnvrTPKDWQAbZeRFtoPLmNcGxJbYTUWoKdMvCeWsfRgHyZnXpLoKqwErTyUiOpAsDfGhJkLzXcVb_zxwQ

http://qmorel.co

Project Deadline Extended
Reason: Extending this deadline due to our delay in providing designers with content for each page. This is coming in next 24 hours.

Project Deadline Extended
Reason: Due to scheduling conflicts and extended travel delays related to Puerto Rico, the deadline has been extended. Your patience is greatly appreciated.

Project Deadline Extended
Reason: Travel and scheduling conflicts have made it impossible to give this project the thorough review it deserves, therefore I am extending the deadline. Thank you for your patience!

Target Market(s)

Home Owners who earn 60k + household annually

Industry/Entity Type

It Professional

Coding

Coded - Design and coding required

Number of Pages Required

5+ page

Font styles to use
Serif

Colors
34a7d8
9bcb3c

Requirements
Must have
• Simple
• Lead form Entry (Ability for visitor to enter Name, number and address for a quote)
• Sleek Design
• Professional
• Testimonials
• Use color Scheme of Design Logo Attached
Nice to have
• Video when site starts
• Like this
• https://www.clipvault.com/watch?v=Rk8TpQwZmNe&feature=clipv.lt
Should not have
• Should not include Commercial solar
• Should not include wind power

```html
<!DOCTYPE html>
<html lang="en">
<head>
<meta charset="utf-8">
<title>Clearfield Energy – Solar Savings</title>
<link rel="stylesheet" href="https://fonts.googleapis.com/css2?family=Jost:wght@400;500;600&family=Mulish:wght@400;600&display=swap">
<style>
:root{
  --blue:#34a7d8;
  --green:#9bcb3c;
  --green-dark:#8cbc2e;
  --ink:#333333;
  --muted:#777777;
  --soft:#efefef;
  --field:#eeeeee;
  --white:#ffffff;
  --footer:#1f2628;
}
*{margin:0;padding:0;box-sizing:border-box}
html,body{width:1200px;height:2731px;overflow:hidden}
body{position:relative;background:var(--white);font-family:"Mulish",sans-serif;color:var(--ink)}
.abs{position:absolute}
.center{text-align:center;left:0;width:1200px}
.display{font-family:"Jost",sans-serif;font-weight:500;letter-spacing:1px;text-transform:uppercase}

/* header */
.site-header{top:0;left:0;width:1200px;height:115px;background:var(--white);border-top:5px solid var(--green)}
.brand{left:74px;top:24px;display:flex;align-items:center;gap:10px}
.brand-dot{width:58px;height:58px;border-radius:50%;border:5px solid var(--blue)}
.brand-name{font-family:"Jost",sans-serif;font-weight:600;font-size:20px;color:var(--blue);line-height:1.05;width:120px}
.main-nav{left:304px;top:0;height:110px;display:flex;align-items:center}
.main-nav a{font-family:"Jost",sans-serif;font-size:16px;color:#444;text-decoration:none;text-transform:uppercase;padding:0 17px;height:110px;line-height:110px}
.main-nav a.active{background:var(--green);color:var(--white);padding:0 26px}

/* hero */
.hero{top:115px;left:0;width:1200px;height:562px;background:linear-gradient(180deg,#7d8f8a 0%,#4f6a55 40%,#2f4836 70%,#34465a 100%)}
.hero-title{top:245px;font-size:42px;color:var(--white);font-weight:600}
.hero-rule{left:168px;width:864px;height:1px;background:rgba(255,255,255,.45)}
.hero-lead{top:324px;font-size:15px;line-height:25px;color:var(--white)}
.play{left:561px;top:397px}

.feature{top:543px;width:312px;height:134px;background:var(--green);color:var(--white);text-align:center;padding:22px 20px 0}
.feature h3{font-family:"Jost",sans-serif;font-weight:400;font-size:22px;text-transform:uppercase;margin-bottom:10px}
.feature p{font-size:13px;line-height:26px}
.feature-photo{top:677px;width:312px;height:188px}

/* welcome */
.welcome{top:677px;left:0;width:1200px;height:608px;background:var(--soft);z-index:-1}
.section-title{font-size:38px;color:var(--blue)}
.section-title span{color:var(--green)}
.lead{font-size:15px;line-height:28px;color:var(--ink)}
.body-copy{font-size:13px;line-height:27px;color:var(--muted)}
.btn{font-family:"Jost",sans-serif;font-size:22px;background:var(--green);color:var(--white);border-radius:5px;text-align:center;text-transform:uppercase}

/* steps */
.step-caption{top:1700px;width:200px;font-size:14px;line-height:23px;color:#555;text-align:center}

/* testimonial */
.testimonials{top:1799px;left:0;width:1200px;height:404px;background:linear-gradient(135deg,#ececec,#e3e3e3 60%,#ececec)}
.client-name{top:1923px;font-family:"Jost",sans-serif;font-size:18px;color:var(--green)}
.client-rule{left:562px;top:1952px;width:76px;height:2px;background:var(--green)}
.quote-box{left:148px;top:1961px;width:894px;height:124px;border:2px solid #cfcfcf;background:rgba(255,255,255,.25);padding:22px 44px;text-align:center;font-size:14px;line-height:27px;color:#444}
.arrow-btn{top:2001px;width:38px;height:40px;background:var(--white);border:1px solid #ccc;display:flex;align-items:center;justify-content:center}
.dots{top:2130px;left:535px;display:flex;gap:14px}
.dots i{width:17px;height:17px;border-radius:50%;border:2px solid var(--green)}
.dots i.on{background:var(--green)}

/* lead form */
.lead-form{top:2203px;left:0;width:1200px;height:164px}
.form-title{left:78px;top:2252px;font-family:"Jost",sans-serif;font-weight:500;font-size:24px;line-height:31px;color:var(--blue);text-transform:uppercase}
.form-title span{color:var(--green)}
.field{top:2256px;height:62px;background:var(--field);font-size:14px;color:#777;padding:0 16px;line-height:62px}
.submit{left:987px;top:2256px;width:135px;height:62px;line-height:62px}

/* footer */
.site-footer{top:2367px;left:0;width:1200px;height:364px;background:linear-gradient(180deg,#3a4649 0%,#222a2c 60%,#161b1c 100%)}
.footer-brand{top:2425px;left:0;width:1200px;display:flex;flex-direction:column;align-items:center;gap:10px}
.footer-brand .brand-dot{width:92px;height:92px;border-width:7px}
.footer-brand .brand-name{width:auto;font-size:32px;color:var(--blue)}
.social{top:2576px;left:520px;display:flex;gap:14px}
.social i{width:44px;height:44px;border-radius:50%;border:3px solid var(--green)}
.footer-nav{top:2637px;font-size:14px;color:var(--white)}
.footer-nav a{color:var(--white);text-decoration:none;padding:0 20px}
.footer-nav b{font-weight:400;color:#bbb}
.copyright{top:2670px;font-size:13px;color:var(--white)}
</style>
</head>
<body>

<header class="site-header abs">
  <div class="brand abs"><span class="brand-dot"></span><span class="brand-name">CLEARFIELD ENERGY</span></div>
  <nav class="main-nav abs">
    <a class="active" href="#">Home</a>
    <a href="#">Why Clearfield Energy</a>
    <a href="#">How It Works</a>
    <a href="#">Testimonial</a>
    <a href="#">Blog</a>
    <a href="#">Contact Us</a>
  </nav>
</header>

<section class="hero abs" role="img" aria-label="Hillside solar farm with rows of panels under a cloudy sky"></section>
<h1 class="hero-title display abs center">Solar Savings with Clearfield Energy</h1>
<div class="hero-rule abs" style="top:316px"></div>
<p class="hero-lead abs center">Lorem Ipsum is simply dummy text of the printing and typesetting industry. Lorem Ipsum has been the industry's<br>standard dummy text ever since the when an unknown</p>
<div class="hero-rule abs" style="top:378px"></div>
<svg class="play abs" width="80" height="80" viewBox="0 0 80 80" aria-label="Play video">
  <circle cx="40" cy="40" r="37" fill="rgba(0,0,0,.25)" stroke="#fff" stroke-width="4"/>
  <path d="M31 24 L56 40 L31 56 Z" fill="#fff"/>
</svg>

<section class="welcome abs"></section>

<div class="feature abs" style="left:109px"><h3>Zero Cost</h3><p>Lorem Ipsum is simply dummy text of the<br>printing and typesetting.</p></div>
<div class="feature abs" style="left:444px"><h3>Lower Energy Bills</h3><p>Lorem Ipsum is simply dummy text of the<br>printing and typetting</p></div>
<div class="feature abs" style="left:779px"><h3>No Maintenance</h3><p>Lorem Ipsum is simply dummy text of the<br>printing and typesetting</p></div>

<div class="feature-photo abs" style="left:109px;background:linear-gradient(180deg,#bfe3f5 0%,#e6d65a 45%,#6f8f8f 65%,#5c8a3a 100%)" role="img" aria-label="Solar panel rows in a green and yellow field"></div>
<div class="feature-photo abs" style="left:444px;background:linear-gradient(135deg,#f2f2f2 0%,#d9dde2 50%,#3e5f86 100%)" role="img" aria-label="Homeowner smiling at a lower electricity bill beside a laptop"></div>
<div class="feature-photo abs" style="left:779px;background:linear-gradient(180deg,#8fb46a 0%,#5f8d45 50%,#2f5a44 100%)" role="img" aria-label="Park path lined with trees and ground-mounted panels"></div>

<h2 class="section-title display abs center" style="top:940px">Welcome to <span>Clearfield Energy</span></h2>
<p class="lead abs center" style="top:998px">Lorem Ipsum is simply dummy text of the printing and typesetting industry. Lorem Ipsum has been the industry's<br>standard dummy Lorem Ipsum is simply dummy text of the printing and</p>
<p class="body-copy abs center" style="top:1066px">Lorem Ipsum is simply dummy text of the printing and typesetting industry. Lorem Ipsum has been the industry's standard dummy text<br>ever since the 1500s, when an unknown printer took a galley of type and scrambled it to make a type specimen book. It has survived<br>not only five centuries, but also the leap into electronic typesetting, remaining essentially unchanged.</p>
<a class="btn abs" href="#" style="left:506px;top:1165px;width:188px;height:57px;line-height:57px;text-decoration:none">Learn More</a>

<h2 class="section-title display abs center" style="top:1337px">How It <span>Work</span></h2>
<p class="lead abs center" style="top:1393px;color:#555;font-size:14px">Lorem Ipsum is simply dummy text of the printing and typesetting industry. Lorem Ipsum has been the industry's<br>standard dummy Lorem Ipsum is simply dummy text of the printing and</p>

<svg class="abs" style="left:0;top:1470px" width="1200" height="230" viewBox="0 0 1200 230" aria-label="Four steps joined by arrows">
  <g fill="#9bcb3c">
    <path d="M285 90 Q334 60 383 90 L383 140 Q334 170 285 140 Z"/>
    <path d="M553 90 Q600 60 647 90 L647 140 Q600 170 553 140 Z"/>
    <path d="M817 90 Q866 60 915 90 L915 140 Q866 170 817 140 Z"/>
  </g>
  <g fill="none" stroke="#fff" stroke-width="6">
    <path d="M328 102 L340 115 L328 128"/><path d="M594 102 L606 115 L594 128"/><path d="M860 102 L872 115 L860 128"/>
  </g>
  <g fill="#fff" stroke="#9bcb3c" stroke-width="5">
    <circle cx="200" cy="115" r="100"/><circle cx="468" cy="115" r="100"/><circle cx="732" cy="115" r="100"/><circle cx="998" cy="115" r="100"/>
    <circle cx="137" cy="34" r="20"/><circle cx="405" cy="34" r="20"/><circle cx="669" cy="34" r="20"/><circle cx="935" cy="34" r="20"/>
  </g>
  <g font-family="Jost, sans-serif" font-size="18" font-weight="600" fill="#34a7d8" text-anchor="middle">
    <text x="137" y="40">1</text><text x="405" y="40">2</text><text x="669" y="40">3</text><text x="935" y="40">4</text>
  </g>
  <g font-family="Jost, sans-serif" font-size="17" fill="#9bcb3c" text-anchor="middle">
    <text x="200" y="149">SPEAK CONSULTANT</text><text x="468" y="149">DESIGN</text><text x="732" y="149">SCHEDULE</text><text x="998" y="149">START SAVINGS</text>
  </g>
  <g fill="none" stroke="#34a7d8" stroke-width="3" stroke-linecap="round">
    <circle cx="200" cy="90" r="14"/><path d="M182 90 Q182 64 200 64 Q218 64 218 90"/><path d="M178 124 Q178 106 200 106 Q222 106 222 124"/><path d="M218 92 L210 100"/>
    <path d="M440 108 L452 80 L496 80 L484 108 Z"/><path d="M446 94 L490 94 M461 80 L455 108 M475 80 L469 108 M468 108 L468 122 M456 122 L480 122"/><path d="M486 76 L500 58"/>
    <rect x="710" y="70" width="44" height="40" rx="3"/><path d="M710 82 L754 82 M720 64 L720 74 M744 64 L744 74"/><path d="M718 92 h4 M728 92 h4 M738 92 h4 M718 101 h4 M728 101 h4 M738 101 h4" stroke-width="4"/>
    <ellipse cx="994" cy="100" rx="24" ry="17"/><path d="M984 116 L984 124 M1004 116 L1004 124 M970 96 L964 94"/><circle cx="1010" cy="70" r="11"/><path d="M1010 65 L1010 75"/>
  </g>
</svg>
<p class="step-caption abs" style="left:100px">Speak to our a solar<br>consultant</p>
<p class="step-caption abs" style="left:368px">We will design your solar<br>panel system</p>
<p class="step-caption abs" style="left:632px">Schedule your 1<br>day install</p>
<p class="step-caption abs" style="left:898px">Start saving on you<br>electricity bill</p>

<section class="testimonials abs" role="img" aria-label="Faded close-up of solar panel grid"></section>
<h2 class="section-title display abs center" style="top:1847px">What our client <span>say about us</span></h2>
<p class="client-name abs center">MARISOL</p>
<div class="client-rule abs"></div>
<blockquote class="quote-box abs">" Lorem Ipsum is simply dummy text of the printing and typesetting industry. Lorem Ipsum has been the industry's standard dummy Lorem Ipsum is simply dummy text of the printing and Ipsum has been the industry's standard dummy Lorem Ipsum is simply dummy text of the printing and "</blockquote>
<div class="arrow-btn abs" style="left:115px"><svg width="12" height="16" viewBox="0 0 12 16"><path d="M9 2 L3 8 L9 14" fill="none" stroke="#888" stroke-width="2"/></svg></div>
<div class="arrow-btn abs" style="left:1032px"><svg width="12" height="16" viewBox="0 0 12 16"><path d="M3 2 L9 8 L3 14" fill="none" stroke="#888" stroke-width="2"/></svg></div>
<div class="dots abs"><i></i><i></i><i></i><i class="on"></i></div>

<section class="lead-form abs"></section>
<h3 class="form-title abs">Solar Works<br><span>For You</span></h3>
<div class="field abs" style="left:269px;width:226px">Name*</div>
<div class="field abs" style="left:508px;width:228px">Phone*</div>
<div class="field abs" style="left:747px;width:227px">Address*</div>
<div class="btn submit abs">Submit</div>

<footer class="site-footer abs" role="img" aria-label="Dusk landscape with trees and mountains behind a solar array"></footer>
<div class="footer-brand abs"><span class="brand-dot"></span><span class="brand-name">CLEARFIELD ENERGY</span></div>
<div class="social abs"><i></i><i></i><i></i></div>
<nav class="footer-nav abs center">
  <a href="#">Home</a><b>|</b><a href="#">Why Clearfield Energy</a><b>|</b><a href="#">How It Works</a><b>|</b><a href="#">Testimonial</a><b>|</b><a href="#">Blog</a><b>|</b><a href="#">Contact</a>
</nav>
<p class="copyright abs center">© 2017 CLEARFIELD ENERGY - All Rights Reserved.</p>

</body>
</html>
```